Flyer Chorkonzert Frühlingsreigen Wolkenhüpfer
Zielgruppe
Wir sind ein gemischter Chor aus der Schweiz unsere Mitglieder sind zwischen 20 und 70 Jahre jung und singen Querbeet durch die Musik von Telmann bis Marrowind.
Weitere Infos www.wolkenhüpfer-chor.ch
Aufgabenstellung
Für unser Konzert mit dem Titel " Frühlingsreigen Wolkenhüpfer" brauchen wir für den Flyer ein Vorderseite Design. Das Konzertprogramm beinhaltet folgende Lieder:
Lanterna/ Varley, Silberner Nebel / Henk Morlitz, Ali di vento/ Lina,Ruth+Beni, Brunnmatt / Gleis,Under the lantern/ Gaukler von Lumm, Nowhere to hide/Marrowind, Winds of the bay/ trad. Irl.,Danse ma plume/trad CH,Never leave the harbour lights behind you/ Gareth Pim, Olas del mar/Tinfold, Paint your Window/Ray Binder.
Idealerweise nimmt das Design Bezug auf den Titel oder auf eines oder mehrere Lieder.
Format: A5 hoch
Text: "Frühlingsreigen Wolkenhüpfer"
Samstag 7. November 2015
17.00 Uhr, Singsaal Lärchenhalde, Uerikon / Stäfa
Sonntag 8. November 2015
17.00 Uhr Kornackersaal, Uetikon am See
Eintritt frei Kollekte

```html
<!DOCTYPE html>
<html lang="de">
<head>
<meta charset="utf-8">
<title>Frühlingsreigen Wolkenhüpfer – Flyer</title>
<link rel="stylesheet" href="https://fonts.googleapis.com/css2?family=Anton&family=Open+Sans:wght@400;600;700&display=swap">
<style>
  :root {
    --maroon: #5c0a2a;
    --maroon-deep: #4a0620;
    --band: #6e0f33;
    --white: #ffffff;
    --red: #e0322c;
    --orange: #f27a22;
    --yellow: #f9c948;
    --pink: #ec4d86;
    --ornament-top: #fff3ea;
    --ornament-bottom: #f49bc8;
  }
  html, body {
    margin: 0;
    padding: 0;
    width: 800px;
    height: 1200px;
    overflow: hidden;
    background: var(--white);
  }
  .flyer {
    position: relative;
    width: 800px;
    height: 1200px;
    overflow: hidden;
    font-family: "Open Sans", sans-serif;
    color: var(--maroon);
  }
  .backdrop {
    position: absolute;
    inset: 0;
    background:
      radial-gradient(ellipse 260px 200px at 190px 470px, rgba(255,236,150,0.85), rgba(255,236,150,0) 70%),
      radial-gradient(ellipse 220px 160px at 720px 330px, rgba(255,220,200,0.7), rgba(255,220,200,0) 70%),
      radial-gradient(ellipse 380px 260px at 260px 900px, rgba(245,110,170,0.75), rgba(245,110,170,0) 70%),
      linear-gradient(165deg, #b8201a 0%, var(--orange) 22%, var(--red) 45%, #e2345a 65%, var(--pink) 85%, #f06a7a 100%);
  }
  .bands {
    position: absolute;
    inset: 0;
  }
  .title-text {
    font-family: "Anton", sans-serif;
    font-size: 78px;
    fill: var(--maroon-deep);
  }
  .ornament {
    position: absolute;
    left: 204px;
    width: 404px;
    height: 64px;
    border-radius: 32px;
  }
  .ornament--top {
    top: 276px;
    background: radial-gradient(ellipse at center, var(--ornament-top) 0%, rgba(255,243,234,0.55) 55%, rgba(255,243,234,0) 100%);
  }
  .ornament--bottom {
    top: 880px;
    background: radial-gradient(ellipse at center, var(--ornament-bottom) 0%, rgba(244,155,200,0.5) 55%, rgba(244,155,200,0) 100%);
  }
  .programme {
    position: absolute;
    top: 392px;
    left: 0;
    width: 800px;
    text-align: center;
  }
  .programme__heading {
    margin: 0 0 26px;
    font-size: 29px;
    font-weight: 700;
    line-height: 1.2;
  }
  .programme__list {
    list-style: none;
    margin: 0;
    padding: 0;
    font-size: 24px;
    line-height: 30.5px;
  }
  .dates {
    position: absolute;
    left: 244px;
    top: 1014px;
    width: 540px;
  }
  .date {
    position: relative;
    padding-left: 52px;
    margin-bottom: 18px;
  }
  .date__icon {
    position: absolute;
    left: 0;
    top: 6px;
    width: 42px;
    height: 58px;
  }
  .date__day {
    margin: 0;
    font-size: 38px;
    font-weight: 600;
    line-height: 40px;
    white-space: nowrap;
  }
  .date__place {
    margin: 0;
    font-size: 20.5px;
    line-height: 24px;
    letter-spacing: 0.6px;
    white-space: nowrap;
  }
  .date__place--wide { letter-spacing: 2px; }
  .admission {
    position: absolute;
    right: 16px;
    top: 1156px;
    margin: 0;
    font-size: 21px;
    font-weight: 700;
    color: #3a3a3a;
    white-space: nowrap;
  }
</style>
</head>
<body>
<div class="flyer">
  <div class="backdrop" role="img" aria-label="Warm red, orange and pink abstract background with soft light flares and translucent music notes"></div>

  <svg class="bands" width="800" height="1200" viewBox="0 0 800 1200" aria-hidden="false">
    <path d="M0,112 C250,60 550,60 800,104 L800,232 C550,202 250,222 0,272 Z" fill="var(--white)"/>
    <path d="M0,272 C250,222 550,202 800,232 L800,244 C550,220 250,244 0,318 Z" fill="var(--maroon-deep)"/>
    <defs>
      <path id="title-curve" d="M14,216 Q400,138 786,206"/>
    </defs>
    <text class="title-text">
      <textPath href="#title-curve" textLength="768" lengthAdjust="spacingAndGlyphs">Frühlingsreigen Wolkenhüpfer</textPath>
    </text>
    <path d="M0,1004 C250,962 550,944 800,962 L800,982 C550,968 250,994 0,1082 Z" fill="var(--band)"/>
    <path d="M0,1082 C250,994 550,968 800,982 L800,1200 L0,1200 Z" fill="var(--white)"/>
  </svg>

  <div class="ornament ornament--top" role="img" aria-label="Decorative white scroll flourish"></div>

  <section class="programme">
    <h2 class="programme__heading">Konzertprogramm:</h2>
    <ul class="programme__list">
      <li>Lanterna/ Varley</li>
      <li>Silberner Nebel / Henk Morlitz</li>
      <li>Ali di vento/ Lina</li>
      <li>Ruth+Beni Brunnmatt / Gleis</li>
      <li>Under the lantern/ Gaukler von Lumm</li>
      <li>Nowhere to hide/Marrowind</li>
      <li>Winds of the bay/ trad. Irl.</li>
      <li>Danse ma plume/trad CH</li>
      <li>Never leave the harbour lights behind you/ Gareth Pim</li>
      <li>Olas del mar/Tinfold</li>
      <li>Paint your Window/Ray Binder</li>
    </ul>
  </section>

  <div class="ornament ornament--bottom" role="img" aria-label="Decorative pink scroll flourish"></div>

  <section class="dates">
    <div class="date">
      <svg class="date__icon" viewBox="0 0 42 58" aria-hidden="true">
        <ellipse cx="13" cy="47" rx="13" ry="9" transform="rotate(-20 13 47)" fill="var(--maroon-deep)"/>
        <rect x="21" y="4" width="5" height="44" fill="var(--maroon-deep)"/>
        <path d="M21,4 C24,14 42,18 38,34 C36,24 30,20 26,20 Z" fill="var(--maroon-deep)"/>
      </svg>
      <p class="date__day">Samstag 7. November 2015</p>
      <p class="date__place">17.00 Uhr, Singsaal Lärchenhalde, Uerikon / Stäfa</p>
    </div>
    <div class="date">
      <svg class="date__icon" viewBox="0 0 42 58" aria-hidden="true">
        <ellipse cx="13" cy="47" rx="13" ry="9" transform="rotate(-20 13 47)" fill="var(--maroon-deep)"/>
        <rect x="21" y="4" width="5" height="44" fill="var(--maroon-deep)"/>
        <path d="M21,4 C24,14 42,18 38,34 C36,24 30,20 26,20 Z" fill="var(--maroon-deep)"/>
      </svg>
      <p class="date__day">Sonntag 8. November 2015</p>
      <p class="date__place date__place--wide">17.00 Uhr Kornackersaal, Uetikon am See</p>
    </div>
  </section>

  <p class="admission">Eintritt frei Kollekte</p>
</div>
</body>
</html>
```